Journeys With Marcella Business Cards

I need a business card design for my upscale Travel Agency.
Attached you can find my logo.
I would like to include the following:
- Name
- Title
- Phone Number
- Email
- Website
- and then something like: Follow us: JourneysWithMarcella (and then social media icons in color).
The logo should be in the front and then also the back.
I am also attaching a design that I liked (mostly for the layout) but open to any suggestions
Industry/Entity Type
Travel Agent
Contact Information for Business Card
Name: Marcella Dorn
Title: Travel Designer / Owner
Phone: 415-927-3308
Email: marcella@journeyswithmarcella-example.com
Website: www.JourneysWithMarcella-example.com
Social Media Handles for FB,IG, Twitter: JourneysWithMarcella
Colors
Designer to choose colors to be used in the design.
Look and feel

```html
<!DOCTYPE html>
<html lang="en">
<head>
<meta charset="utf-8">
<title>Journeys With Marcella – Business Cards</title>
<link rel="stylesheet" href="https://fonts.googleapis.com/css2?family=Libre+Baskerville:wght@400;700&family=Roboto:wght@500&display=swap">
<style>
  :root {
    --apricot: #f4aa5c;
    --card-white: #ffffff;
    --ink-grey: #555555;
    --rule-grey: #7a7a7a;
    --backdrop: #e6e6e6;
    --shadow: rgba(0, 0, 0, 0.18);
  }
  * { margin: 0; padding: 0; box-sizing: border-box; }
  html, body {
    width: 1200px;
    height: 900px;
    overflow: hidden;
    background: var(--backdrop);
  }
  .sheet {
    position: relative;
    width: 1200px;
    height: 900px;
  }
  .card {
    position: absolute;
    left: 320px;
    width: 560px;
    height: 320px;
    box-shadow: 0 6px 18px var(--shadow);
  }

  /* Back of card */
  .card-back {
    top: 100px;
    background: var(--apricot);
    color: var(--card-white);
  }
  .card-back .brand-name {
    position: absolute;
    top: 96px;
    left: 0;
    width: 100%;
    text-align: center;
    font-family: "Libre Baskerville", serif;
    font-weight: 700;
    font-size: 36px;
    line-height: 1.2;
  }
  .card-back .follow-row {
    position: absolute;
    left: 0;
    top: 232px;
    width: 100%;
    display: flex;
    justify-content: center;
    align-items: center;
    gap: 8px;
    font-family: "Roboto", sans-serif;
    font-weight: 500;
    font-size: 15px;
    letter-spacing: 0.3px;
  }
  .follow-row .dot {
    width: 16px;
    height: 16px;
    border-radius: 50%;
    background: var(--card-white);
  }

  /* Front of card */
  .card-front {
    top: 480px;
    background: var(--card-white);
  }
  .card-front .brand-lockup {
    position: absolute;
    top: 40px;
    right: 26px;
    display: flex;
    align-items: center;
    gap: 10px;
  }
  .brand-lockup .brand-square {
    width: 22px;
    height: 22px;
    background: var(--apricot);
  }
  .brand-lockup .brand-name {
    font-family: "Libre Baskerville", serif;
    font-weight: 700;
    font-size: 21px;
    color: var(--apricot);
  }
  .card-front .person {
    position: absolute;
    left: 30px;
    top: 138px;
    font-family: "Libre Baskerville", serif;
  }
  .person .person-name {
    font-weight: 700;
    font-size: 22px;
    color: var(--apricot);
    line-height: 1.2;
  }
  .person .person-title {
    font-size: 13px;
    font-weight: 700;
    color: var(--ink-grey);
    margin-top: 2px;
  }
  .card-front .divider {
    position: absolute;
    left: 26px;
    right: 26px;
    top: 206px;
    height: 2px;
    background: var(--rule-grey);
  }
  .card-front .contact-list {
    position: absolute;
    right: 26px;
    top: 222px;
    list-style: none;
    font-family: "Libre Baskerville", serif;
    font-size: 12.5px;
    color: var(--ink-grey);
    text-align: right;
  }
  .contact-list li {
    display: flex;
    justify-content: flex-end;
    align-items: center;
    gap: 8px;
    line-height: 22px;
  }
  .contact-list svg {
    width: 13px;
    height: 13px;
    flex: none;
  }
</style>
</head>
<body>
<main class="sheet">

  <section class="card card-back" aria-label="Card back">
    <p class="brand-name">Journeys With Marcella</p>
    <p class="follow-row"><span class="dot"></span>JourneysWithMarcella</p>
  </section>

  <section class="card card-front" aria-label="Card front">
    <div class="brand-lockup">
      <span class="brand-square"></span>
      <span class="brand-name">Journeys With Marcella</span>
    </div>

    <div class="person">
      <p class="person-name">Marcella Dorn</p>
      <p class="person-title">Travel Designer / Owner</p>
    </div>

    <div class="divider"></div>

    <ul class="contact-list">
      <li>415-927-3308
        <svg viewBox="0 0 24 24" aria-hidden="true"><path fill="#f4aa5c" d="M6.6 10.8a15 15 0 0 0 6.6 6.6l2.2-2.2a1 1 0 0 1 1-.25 11.4 11.4 0 0 0 3.6.57 1 1 0 0 1 1 1V20a1 1 0 0 1-1 1A17 17 0 0 1 3 4a1 1 0 0 1 1-1h3.5a1 1 0 0 1 1 1c0 1.25.2 2.45.57 3.57a1 1 0 0 1-.25 1z"/></svg>
      </li>
      <li>marcella@journeyswithmarcella-example.com
        <svg viewBox="0 0 24 24" aria-hidden="true"><rect x="2" y="5" width="20" height="14" fill="#f4aa5c"/><path d="M2 5l10 8 10-8" fill="none" stroke="#ffffff" stroke-width="1.6"/></svg>
      </li>
      <li>www.JourneysWithMarcella-example.com
        <svg viewBox="0 0 24 24" aria-hidden="true"><circle cx="12" cy="12" r="10" fill="#f4aa5c"/><path d="M2 12h20M12 2c3 3 3 17 0 20M12 2c-3 3-3 17 0 20" fill="none" stroke="#ffffff" stroke-width="1.4"/></svg>
      </li>
    </ul>
  </section>

</main>
</body>
</html>
```